Small Business Consulting Firm Needs Business Card Design

Need a sleek modern business card with 2 sides matching the colors of our logo. We will be placing these with a mailer we are sending out. These business cards will only ever be given to business owners. We operate helping businesses who are struggling with cash flow or finances. If the green and blue design needs to be moved to the right of "Harborline Crest Consulting" for aesthetic purposes that is ok. We will need an editable file if possible. We would like to include the reps name, email, website, and phone number. For now just use Peter Vance, pvance@harborlinecrest.com, www.harborlinecrest.com, and 833-555-0172.

```html
<!DOCTYPE html>
<html lang="en">
<head>
<meta charset="utf-8">
<title>Harborline Crest Consulting – Business Card</title>
<link rel="stylesheet" href="https://fonts.googleapis.com/css2?family=Montserrat:wght@400&family=Exo+2:wght@400;500;700&display=swap">
<style>
  :root {
    --stage: #e9eaec;
    --card-dark-top: #4b4b4d;
    --card-dark-bottom: #2d2d2f;
    --card-light: #ffffff;
    --ink: #3a3a3c;
    --ink-soft: #555557;
    --brand-blue: #1d7fc9;
    --brand-green: #6bbd3e;
    --rule: #4a4a4c;
  }
  * { box-sizing: border-box; margin: 0; padding: 0; }
  html, body {
    width: 1200px; height: 1000px; overflow: hidden;
    background: var(--stage);
  }
  .canvas { position: relative; width: 1200px; height: 1000px; }

  .card {
    position: absolute; left: 210px;
    width: 780px; height: 446px;
    border-radius: 4px;
    box-shadow: 0 10px 28px rgba(0,0,0,0.18);
    overflow: hidden;
  }

  /* Back side */
  .card--back {
    top: 36px;
    background: linear-gradient(160deg, var(--card-dark-top), var(--card-dark-bottom));
  }
  .card--back .wordmark {
    position: absolute; left: 64px; bottom: 70px;
    display: flex; align-items: center; gap: 22px;
  }
  .card--back .wordmark__square {
    width: 44px; height: 44px; background: var(--brand-green);
  }
  .wordmark__text {
    font-family: "Montserrat", sans-serif; font-weight: 400;
    text-transform: uppercase; line-height: 1;
  }
  .card--back .wordmark__text { color: #ffffff; }
  .card--back .wordmark__name { font-size: 40px; letter-spacing: 3px; display: block; }
  .card--back .wordmark__tag { font-size: 17px; letter-spacing: 11px; display: block; margin-top: 10px; padding-left: 60px; }

  /* Front side */
  .card--front {
    top: 518px;
    background: var(--card-light);
  }
  .card--front .wordmark {
    position: absolute; left: 56px; top: 52px;
    display: flex; align-items: center; gap: 16px;
  }
  .card--front .wordmark__square {
    width: 30px; height: 30px; background: var(--brand-green);
  }
  .card--front .wordmark__text { color: var(--ink); }
  .card--front .wordmark__name { font-size: 27px; letter-spacing: 2px; display: block; }
  .card--front .wordmark__tag { font-size: 12px; letter-spacing: 8px; display: block; margin-top: 7px; padding-left: 42px; }

  .divider {
    position: absolute; left: 56px; right: 56px; top: 150px;
    height: 2px; background: linear-gradient(90deg, rgba(74,74,76,0), var(--rule) 30%);
  }

  .rep { position: absolute; left: 56px; top: 178px; font-family: "Exo 2", sans-serif; }
  .rep__name { font-size: 30px; font-weight: 700; color: var(--brand-blue); line-height: 1.1; }
  .rep__title { font-size: 18px; font-weight: 500; color: var(--ink); margin-top: 4px; }
  .rep__rule { width: 230px; height: 2px; background: var(--rule); margin-top: 16px; }

  .contact { list-style: none; margin-top: 16px; }
  .contact__item {
    display: flex; align-items: center; gap: 14px;
    font-size: 20px; font-weight: 400; color: var(--ink-soft);
    height: 32px;
  }
  .contact__icon { width: 20px; height: 20px; fill: var(--brand-blue); flex: none; }
</style>
</head>
<body>
<main class="canvas">

  <section class="card card--back" aria-label="Card back">
    <div class="wordmark">
      <span class="wordmark__square"></span>
      <p class="wordmark__text">
        <span class="wordmark__name">Harborline Crest</span>
        <span class="wordmark__tag">Consulting</span>
      </p>
    </div>
  </section>

  <section class="card card--front" aria-label="Card front">
    <div class="wordmark">
      <span class="wordmark__square"></span>
      <p class="wordmark__text">
        <span class="wordmark__name">Harborline Crest</span>
        <span class="wordmark__tag">Consulting</span>
      </p>
    </div>

    <div class="divider"></div>

    <div class="rep">
      <h1 class="rep__name">Peter Vance</h1>
      <p class="rep__title">Manager</p>
      <div class="rep__rule"></div>
      <ul class="contact">
        <li class="contact__item">
          <svg class="contact__icon" viewBox="0 0 24 24" aria-hidden="true"><path d="M6.6 10.8a15.1 15.1 0 0 0 6.6 6.6l2.2-2.2c.3-.3.7-.4 1-.2 1.1.4 2.3.6 3.6.6.6 0 1 .4 1 1V20c0 .6-.4 1-1 1C10.6 21 3 13.4 3 4c0-.6.4-1 1-1h3.5c.6 0 1 .4 1 1 0 1.3.2 2.5.6 3.6.1.3 0 .7-.2 1z"/></svg>
          <span>833-555-0172</span>
        </li>
        <li class="contact__item">
          <svg class="contact__icon" viewBox="0 0 24 24" aria-hidden="true"><path d="M2 5h20v14H2z M2 5l10 8 10-8" fill="none" stroke="var(--brand-blue)" stroke-width="0"/><path d="M2 5h20L12 12.5z"/><path d="M2 7l10 7.5L22 7v12H2z"/></svg>
          <span>pvance@harborlinecrest.com</span>
        </li>
        <li class="contact__item">
          <svg class="contact__icon" viewBox="0 0 24 24" aria-hidden="true"><circle cx="12" cy="12" r="10"/><path d="M2 12h20M12 2c3 3 3 17 0 20M12 2c-3 3-3 17 0 20" fill="none" stroke="#fff" stroke-width="1.4"/></svg>
          <span>www.harborlinecrest.com</span>
        </li>
      </ul>
    </div>
  </section>

</main>
</body>
</html>
```